Crestline Gas and Plumbing Business Card Design

I am after a business card design for my plumbing business called 'Crestline Gas & Plumbing'. I do all types of plumbing and gas work and specialise in general maintenance plumbing. Would like to see designs using current logo

Industry/Entity Type

Plumbing

Contact Information for Business Card

Name - Dale Whitcombe
Phone number - 0455163027
Email - admin@crestlinegasandplumbing.example.com.au
ABN - 68204915336

```html
<!DOCTYPE html>
<html lang="en">
<head>
<meta charset="utf-8">
<title>Crestline Gas &amp; Plumbing – Business Card</title>
<link rel="stylesheet" href="https://fonts.googleapis.com/css2?family=Russo+One&family=Open+Sans:wght@400&display=swap">
<style>
  :root {
    --backdrop: #2b2b2b;
    --card-white: #ffffff;
    --brand-blue: #2a4fa8;
    --accent-orange: #f08a1c;
    --rule-violet: #5a5db4;
    --text-grey: #3d3d3d;
    --back-deep: #2c3497;
    --back-bright: #2a86d2;
  }
  * { margin: 0; padding: 0; box-sizing: border-box; }
  html, body {
    width: 1200px; height: 802px; overflow: hidden;
    background: var(--backdrop);
  }
  .stage { position: relative; width: 1200px; height: 802px; }
  .card {
    position: absolute; top: 274px; width: 447px; height: 255px;
    border-radius: 12px; overflow: hidden;
  }
  .card-front { left: 135px; background: var(--card-white); }
  .card-back {
    left: 622px;
    background: linear-gradient(180deg, var(--back-deep) 0%, var(--back-bright) 52%, var(--back-deep) 100%);
  }
  .holder-name {
    position: absolute; right: 32px; top: 26px;
    font-family: "Russo One", sans-serif; font-size: 14px;
    letter-spacing: 0.5px; color: var(--brand-blue);
  }
  .brand-lockup {
    position: absolute; left: 0; right: 0;
    display: flex; align-items: center; justify-content: center; gap: 9px;
  }
  .card-front .brand-lockup { top: 92px; }
  .card-back .brand-lockup { top: 112px; }
  .brand-dot { width: 16px; height: 16px; border-radius: 50%; }
  .card-front .brand-dot { background: var(--accent-orange); }
  .card-back .brand-dot { background: #ffffff; }
  .brand-name {
    font-family: "Russo One", sans-serif; font-size: 19px; white-space: nowrap;
  }
  .card-front .brand-name { color: var(--brand-blue); }
  .card-back .brand-name { color: #ffffff; }
  .divider {
    position: absolute; left: 31px; right: 32px; top: 183px;
    height: 2px; background: var(--rule-violet);
  }
  .contact-list {
    position: absolute; left: 0; right: 0; top: 196px;
    list-style: none; text-align: center;
    font-family: "Open Sans", sans-serif; font-size: 12px; line-height: 14.5px;
    color: var(--text-grey);
  }
  .contact-list li { display: flex; justify-content: center; align-items: center; gap: 5px; }
  .contact-icon { width: 10px; height: 10px; }
  .abn-label { color: var(--accent-orange); }
</style>
</head>
<body>
<main class="stage">
  <section class="card card-front" aria-label="Business card front">
    <p class="holder-name">DALE WHITCOMBE</p>
    <div class="brand-lockup">
      <span class="brand-dot"></span>
      <span class="brand-name">Crestline Gas &amp; Plumbing</span>
    </div>
    <div class="divider"></div>
    <ul class="contact-list">
      <li>
        <svg class="contact-icon" viewBox="0 0 10 10" aria-hidden="true">
          <circle cx="5" cy="5" r="5" fill="#f08a1c"/>
          <path d="M3.2 2.6 L4.2 2.6 L4.6 3.8 L4 4.3 Q4.6 5.6 5.8 6.1 L6.3 5.5 L7.4 5.9 L7.4 6.9 Q5.4 7.2 4 5.9 Q2.8 4.6 3.2 2.6 Z" fill="#fff"/>
        </svg>
        <span>0455163027</span>
      </li>
      <li>
        <svg class="contact-icon" viewBox="0 0 10 10" aria-hidden="true">
          <circle cx="5" cy="5" r="5" fill="#f08a1c"/>
          <circle cx="5" cy="5" r="2.8" fill="none" stroke="#fff" stroke-width="0.8"/>
          <line x1="2.2" y1="5" x2="7.8" y2="5" stroke="#fff" stroke-width="0.7"/>
          <ellipse cx="5" cy="5" rx="1.2" ry="2.8" fill="none" stroke="#fff" stroke-width="0.7"/>
        </svg>
        <span>admin@crestlinegasandplumbing.example.com.au</span>
      </li>
      <li><span><span class="abn-label">ABN</span> - 68204915336</span></li>
    </ul>
  </section>

  <section class="card card-back" aria-label="Business card back">
    <div class="brand-lockup">
      <span class="brand-dot"></span>
      <span class="brand-name">Crestline Gas &amp; Plumbing</span>
    </div>
  </section>
</main>
</body>
</html>
```